Resume

I am an industrial designer that has just graduated from school. I have been trying to brand myself when applying to companies. Even though I know of the basic principles in graphic design I have difficulty executing it. I have supplied my logo (which is simple but clean) and two forms of my resume I was playing around with. One is Mostly text the other has more color and is more graphic. I would like something in the middle. I would like to have a creative graph that is easy to read that displays my skills.
Updates

Project Deadline Extended
Reason: Some of the designers were asking for an extra day. I gave it 3.

Industry/Entity Type

Graphic Design

```html
<!DOCTYPE html>
<html lang="en">
<head>
<meta charset="utf-8">
<title>Owen Tarrant – Resume</title>
<link rel="stylesheet" href="https://fonts.googleapis.com/css2?family=Open+Sans:ital,wght@0,300;0,400;0,600;0,700;1,400&display=swap">
<style>
  :root {
    --ink: #111111;
    --paper: #ffffff;
    --brand-red: #b83a2b;
    --education: #a47f70;
    --work: #a34f55;
    --skills: #8c787b;
    --contact: #dd9dbd;
    --software: #b28ea8;
    --node: #5a5a5a;
    --photo-top: #8a6a4e;
    --photo-bottom: #3b2c22;
    --star-empty: #6b6b6b;
  }
  html, body { margin: 0; padding: 0; overflow: hidden; background: var(--paper); }
  .resume {
    position: relative; width: 927px; height: 1200px; overflow: hidden;
    background: var(--paper); color: var(--ink);
    font-family: "Open Sans", sans-serif;
  }
  .at { position: absolute; white-space: nowrap; transform: translateY(-50%); line-height: 1.2; margin: 0; }

  /* Header */
  .brand-mark {
    position: absolute; left: 55px; top: 55px; width: 125px; height: 70px;
    background: var(--brand-red); color: var(--paper);
    display: flex; align-items: center; justify-content: center;
    font-size: 30px; font-weight: 400; letter-spacing: 1px;
  }
  .greeting { left: 193px; top: 70px; font-size: 32px; font-weight: 300; }
  .headline { left: 193px; top: 114px; font-size: 34px; font-weight: 300; }
  .headline strong { font-weight: 400; }
  .portrait {
    position: absolute; left: 55px; top: 144px; width: 122px; height: 139px;
    background: linear-gradient(160deg, var(--photo-top), var(--photo-bottom));
  }
  .fact-label { left: 193px; font-size: 17px; font-weight: 700; }
  .fact-value { left: 301px; font-size: 17px; }
  .header-divider { position: absolute; left: 521px; top: 144px; width: 1px; height: 139px; background: var(--ink); }
  .intro { position: absolute; left: 537px; top: 143px; width: 330px; margin: 0; font-size: 16.3px; line-height: 21.6px; }
  .rule { position: absolute; left: 55px; top: 303px; width: 817px; height: 6px; background: var(--ink); }

  /* Panels */
  .panel { position: absolute; width: 392px; border-radius: 0 22px 0 22px; }
  .panel-education { left: 55px; top: 331px; height: 291px; background: var(--education); }
  .panel-work { left: 481px; top: 331px; height: 545px; background: var(--work); }
  .panel-skills { left: 55px; top: 669px; height: 291px; background: var(--skills); }
  .panel-contact { left: 55px; top: 1007px; height: 137px; background: var(--contact); }
  .panel-software { left: 481px; top: 924px; height: 220px; background: var(--software); }
  .panel-title { font-size: 25px; font-weight: 600; letter-spacing: 5px; }
  .timeline { position: absolute; left: 0; top: 0; }

  .year { font-size: 16.5px; }
  .entry-name { font-size: 17px; }
  .entry-role { font-size: 13.5px; font-style: italic; }
  .align-right { text-align: right; transform: translate(-100%, -50%); }
  .side-note { font-size: 9.5px; font-style: italic; transform: translate(-50%, -50%) rotate(-90deg); }

  .skill-name { left: 49px; font-size: 16.5px; font-weight: 700; }
  .stars { position: absolute; left: 201px; transform: translateY(-50%); }
  .ability { font-size: 16.5px; }

  .contact-label { left: 28px; font-size: 16.5px; font-weight: 700; }
  .contact-value { left: 138px; font-size: 16.5px; }
  .tool { font-size: 16.5px; font-weight: 600; }
</style>
</head>
<body>
<main class="resume">
  <svg width="0" height="0" style="position:absolute" aria-hidden="true">
    <defs>
      <symbol id="star" viewBox="0 0 20 20">
        <polygon points="10,1 12.6,7.2 19.3,7.6 14.2,11.9 15.8,18.5 10,15 4.2,18.5 5.8,11.9 0.7,7.6 7.4,7.2" stroke="#222" stroke-width="1.2" stroke-linejoin="round"/>
      </symbol>
    </defs>
  </svg>

  <header>
    <div class="brand-mark">ot</div>
    <div class="at greeting">Hi!</div>
    <h1 class="at headline">I am <strong>Owen Tarrant</strong></h1>
    <div class="portrait" role="img" aria-label="Portrait photo of Owen Tarrant"></div>

    <div class="at fact-label" style="top:152px">Nationality</div><div class="at fact-value" style="top:152px">United States</div>
    <div class="at fact-label" style="top:183px">Location</div><div class="at fact-value" style="top:183px">Florida</div>
    <div class="at fact-label" style="top:213px">Birthday</div><div class="at fact-value" style="top:213px">9 April 1988</div>
    <div class="at fact-label" style="top:243px">Education</div><div class="at fact-value" style="top:243px">Major in Industrial Design</div>
    <div class="at fact-label" style="top:274px">Availabilty</div><div class="at fact-value" style="top:274px">Full time</div>

    <div class="header-divider"></div>
    <p class="intro">[Place for own intro text if wanted]<br>Lorem ipsum dolor sit amet, consectetur adipiscing elit. Morbi viverra lacus sed ipsum eleifend, vitae vehicula mi ultricies. Sed eleifend blandit urna a facilisis. Morbi pharetra ac ipsum eu placerat.</p>
    <div class="rule"></div>
  </header>

  <section class="panel panel-education">
    <svg class="timeline" width="392" height="291" aria-hidden="true">
      <line x1="110" y1="62" x2="110" y2="262" stroke="#000" stroke-width="6"/>
      <circle cx="110" cy="118" r="18" fill="var(--node)" stroke="#000" stroke-width="4"/>
      <circle cx="110" cy="209" r="18" fill="var(--node)" stroke="#000" stroke-width="4"/>
    </svg>
    <h2 class="at panel-title" style="left:49px;top:40px">Education</h2>
    <div class="at year align-right" style="left:89px;top:119px">2006</div>
    <div class="at entry-name" style="left:131px;top:109px">Brevard Coast College</div>
    <div class="at entry-role" style="left:131px;top:130px">Drafting and Design</div>
    <div class="at year align-right" style="left:89px;top:210px">2010</div>
    <div class="at entry-name" style="left:131px;top:200px">Atlantic College of</div>
    <div class="at entry-name" style="left:131px;top:222px">Art and Design</div>
    <div class="at entry-role" style="left:131px;top:242px">Industrial Design</div>
  </section>

  <section class="panel panel-work">
    <svg class="timeline" width="392" height="545" aria-hidden="true">
      <line x1="279" y1="50" x2="279" y2="529" stroke="#000" stroke-width="6"/>
      <circle cx="279" cy="104" r="18" fill="var(--node)" stroke="#000" stroke-width="4"/>
      <circle cx="279" cy="196" r="18" fill="var(--node)" stroke="#000" stroke-width="4"/>
      <circle cx="279" cy="287" r="18" fill="var(--node)" stroke="#000" stroke-width="4"/>
      <circle cx="279" cy="380" r="18" fill="var(--node)" stroke="#000" stroke-width="4"/>
      <circle cx="279" cy="471" r="18" fill="var(--node)" stroke="#000" stroke-width="4"/>
    </svg>
    <h2 class="at panel-title" style="left:35px;top:26px">Work history</h2>

    <div class="at entry-name align-right" style="left:259px;top:95px">Palmetto Entertainment Inc.</div>
    <div class="at entry-role align-right" style="left:259px;top:114px">Assistant manager</div>
    <div class="at year" style="left:301px;top:105px">2004</div>

    <div class="at entry-name align-right" style="left:259px;top:187px">Harbor Furniture Outlet</div>
    <div class="at entry-role align-right" style="left:259px;top:206px">Sales team manager</div>
    <div class="at year" style="left:301px;top:197px">2010</div>

    <div class="at entry-name align-right" style="left:259px;top:279px">Wayfare Traders</div>
    <div class="at entry-role align-right" style="left:259px;top:297px">Sales associate</div>
    <div class="at year" style="left:301px;top:288px">2011</div>

    <div class="at side-note" style="left:124px;top:379px">Internship</div>
    <div class="at entry-name align-right" style="left:257px;top:362px">Coastal Heron</div>
    <div class="at entry-role align-right" style="left:257px;top:381px">Designing signs &amp;</div>
    <div class="at entry-role align-right" style="left:257px;top:398px">displays</div>
    <div class="at year" style="left:301px;top:381px">2013</div>

    <div class="at entry-name align-right" style="left:259px;top:461px">Freelance Designer</div>
    <div class="at year" style="left:301px;top:472px">2013</div>
  </section>

  <section class="panel panel-skills">
    <h2 class="at panel-title" style="left:49px;top:21px">Skills</h2>

    <div class="at skill-name" style="top:61px">Proffessionalism</div>
    <svg class="stars" style="top:61px" width="130" height="22" role="img" aria-label="4 of 5">
      <use href="#star" x="2" y="1" width="20" height="20" fill="#fff"/><use href="#star" x="28" y="1" width="20" height="20" fill="#fff"/><use href="#star" x="54" y="1" width="20" height="20" fill="#fff"/><use href="#star" x="80" y="1" width="20" height="20" fill="#fff"/><use href="#star" x="106" y="1" width="20" height="20" fill="var(--star-empty)"/>
    </svg>
    <div class="at skill-name" style="top:91px">Organization</div>
    <svg class="stars" style="top:91px" width="130" height="22" role="img" aria-label="5 of 5">
      <use href="#star" x="2" y="1" width="20" height="20" fill="#fff"/><use href="#star" x="28" y="1" width="20" height="20" fill="#fff"/><use href="#star" x="54" y="1" width="20" height="20" fill="#fff"/><use href="#star" x="80" y="1" width="20" height="20" fill="#fff"/><use href="#star" x="106" y="1" width="20" height="20" fill="#fff"/>
    </svg>
    <div class="at skill-name" style="top:122px">Creativity</div>
    <svg class="stars" style="top:122px" width="130" height="22" role="img" aria-label="5 of 5">
      <use href="#star" x="2" y="1" width="20" height="20" fill="#fff"/><use href="#star" x="28" y="1" width="20" height="20" fill="#fff"/><use href="#star" x="54" y="1" width="20" height="20" fill="#fff"/><use href="#star" x="80" y="1" width="20" height="20" fill="#fff"/><use href="#star" x="106" y="1" width="20" height="20" fill="#fff"/>
    </svg>
    <div class="at skill-name" style="top:152px">Communication</div>
    <svg class="stars" style="top:152px" width="130" height="22" role="img" aria-label="4 of 5">
      <use href="#star" x="2" y="1" width="20" height="20" fill="#fff"/><use href="#star" x="28" y="1" width="20" height="20" fill="#fff"/><use href="#star" x="54" y="1" width="20" height="20" fill="#fff"/><use href="#star" x="80" y="1" width="20" height="20" fill="#fff"/><use href="#star" x="106" y="1" width="20" height="20" fill="var(--star-empty)"/>
    </svg>
    <div class="at skill-name" style="top:183px">Teamwork</div>
    <svg class="stars" style="top:183px" width="130" height="22" role="img" aria-label="5 of 5">
      <use href="#star" x="2" y="1" width="20" height="20" fill="#fff"/><use href="#star" x="28" y="1" width="20" height="20" fill="#fff"/><use href="#star" x="54" y="1" width="20" height="20" fill="#fff"/><use href="#star" x="80" y="1" width="20" height="20" fill="#fff"/><use href="#star" x="106" y="1" width="20" height="20" fill="#fff"/>
    </svg>

    <div class="at ability" style="left:46px;top:222px">✓Conceptualizing</div>
    <div class="at ability" style="left:206px;top:222px">✓Welding</div>
    <div class="at ability" style="left:46px;top:247px">✓Sketching</div>
    <div class="at ability" style="left:206px;top:247px">✓Model making</div>
    <div class="at ability" style="left:46px;top:273px">✓3D Modeling</div>
    <div class="at ability" style="left:206px;top:273px">✓Prototyping</div>
  </section>

  <section class="panel panel-contact">
    <div class="at contact-label" style="top:24px">Phone</div><div class="at contact-value" style="top:24px">+15550148236</div>
    <div class="at contact-label" style="top:55px">Email</div><div class="at contact-value" style="top:55px">owen.tarrant@mailbox.net</div>
    <div class="at contact-label" style="top:84px">Website</div><div class="at contact-value" style="top:84px">www.folioshelf.net/otarrant</div>
    <div class="at contact-label" style="top:115px">Social</div><div class="at contact-value" style="top:115px">www.socialpage.net/otarrant</div>
  </section>

  <section class="panel panel-software">
    <h2 class="at panel-title" style="left:35px;top:38px">Software</h2>
    <div class="at tool" style="left:35px;top:72px">FormCAD</div>
    <div class="at tool" style="left:35px;top:103px">Curvo 3D</div>
    <div class="at tool" style="left:35px;top:134px">Lumashot</div>
    <div class="at tool" style="left:35px;top:164px">Shop Skills</div>
    <div class="at tool" style="left:35px;top:195px">PixelDesk</div>
    <div class="at tool" style="left:206px;top:72px">PageSet</div>
    <div class="at tool" style="left:206px;top:103px">VectorLab</div>
    <div class="at tool" style="left:206px;top:134px">MeshBlend</div>
    <div class="at tool" style="left:206px;top:164px">OfficeSuite</div>
  </section>
</main>
</body>
</html>
```